Wordpress website design needed for website re-launch of established lawn care company (Design mu...

We are a gardening company and are separating and re-launching the lawn care part of the company. We already have a non-wordpress website which includes a lawn care section and therefore contains all the content needed for the new website. We essentially need to take that content (over 6 pages) and re-create it into a new, modern and visually appealing design in our new Wordpress website. We use Divi and therefore the new design must be built and be compatible with the Divi theme. However, I am not looking to use a pre-built Divi layout or any template offered by Quarry Layouts. I could easily do that myself. I'm looking for a bespoke design.

The pages of our current website that need to be re-designed within Divi are:
http://www.brackettgrounds.co.uk/lawncare/7281604452
http://www.brackettgrounds.co.uk/lawnfertilisers/7281619038
http://www.brackettgrounds.co.uk/lawnaeration/7281652271
http://www.brackettgrounds.co.uk/lawnscarification/7281658815
http://www.brackettgrounds.co.uk/lawntreatments/7281663340
http://www.brackettgrounds.co.uk/lawncarepackages/7281619177

Our Wordpress site is already set up with Veltra with the domain www.brackettturfcare.co.uk and as I say, uses the Divi theme. I am not sure how you will deliver your designs but it must be using or compatible with Divi.

Target Market(s)

Homeowners ages 30+

Industry/Entity Type

Gardener

Font styles to use
Sans Serif

Colors
a64599
9bcb3c

Requirements
Must have
• The new site must still use our existing company colours - purple and green. Have a look on www.brackettgrounds.co.uk to get the right colours.
• Must be mobile responsive
Nice to have
• We want a fresh and modern new look for our new lawn care website.
• I have also attached a picture of our van and lawn care flyers so you can see what our current branding and style looks like in case it helps with your design.
Should not have
• Please don't just submit pre-designed templates that bear no relevance to my brief or requirements above. I could very easily go and install a pre-designed template and plug my content in but that's not what I'm looking for. Submissions should take into consideration my existing content, my brand colours and my logo as a minimum.

```html
<!DOCTYPE html>
<html lang="en">
<head>
<meta charset="utf-8">
<title>Brackett Grounds Services – Garden Maintenance</title>
<link rel="stylesheet" href="https://fonts.googleapis.com/css2?family=Bitter:wght@400;500;700&family=Open+Sans:wght@400;600;700&display=swap">
<style>
:root{
  --purple:#8e3f8a;
  --purple-light:#a64599;
  --green:#3f9a3a;
  --green-bright:#9bcb3c;
  --green-dark:#24452a;
  --ink:#3a3a3a;
  --muted:#7a7a7a;
  --paper:#ffffff;
  --soft:#f4f5f2;
  --footer:#2b2b2b;
  --footer-deep:#1e1e1e;
}
*{box-sizing:border-box;margin:0;padding:0}
html,body{width:1200px;height:2644px;overflow:hidden}
body{font-family:"Open Sans",Arial,sans-serif;color:var(--ink);background:var(--paper);font-size:15px;line-height:1.6}
.btn{display:inline-block;border-radius:24px;padding:12px 30px;color:#fff;font-size:15px;font-weight:600;text-decoration:none}
.btn-green{background:var(--green)}
.btn-purple{background:var(--purple)}

/* top bar */
.topbar{height:34px;background:var(--green-dark);color:#fff;font-size:12px;display:flex;align-items:center;padding:0 40px;position:relative}
.topbar span{margin-right:26px;display:flex;align-items:center;gap:6px}
.topbar .call{position:absolute;right:40px;top:0;height:34px;background:var(--green);padding:0 28px;display:flex;align-items:center;font-weight:700}

/* header */
.header{height:140px;position:relative;border-bottom:1px solid #e6e6e6}
.tagline{position:absolute;right:40px;top:0;background:var(--purple);color:#fff;font-size:14px;font-weight:600;padding:8px 24px}
.brand{position:absolute;left:40px;top:22px;display:flex;align-items:center;gap:12px}
.brand i{width:30px;height:30px;border-radius:50%;background:var(--green)}
.brand b{font-family:"Bitter",Georgia,serif;font-size:30px;font-weight:700;color:var(--green-dark);line-height:1.1}
.nav{position:absolute;right:40px;top:70px;display:flex;gap:26px;font-size:14px;color:var(--ink)}
.nav a{color:inherit;text-decoration:none}
.nav a.active{color:var(--green);font-weight:600}

/* hero */
.hero{height:386px;position:relative;background:linear-gradient(100deg,#6b4a33 0%,#8a6a4a 35%,#4f6b3a 65%,#355129 100%)}
.hero-text{position:absolute;left:630px;top:60px;width:500px;color:#fff}
.hero-text h1{font-family:"Bitter",Georgia,serif;font-weight:500;font-size:40px;line-height:1.25;margin-bottom:16px}
.hero-text p{font-size:14px;margin-bottom:22px;max-width:420px}

/* services */
.services{height:270px;padding:30px 0 0 140px}
.eyebrow{color:var(--purple);font-weight:700;font-size:13px;letter-spacing:.5px}
.services h2{font-family:"Bitter",Georgia,serif;color:var(--green);font-size:26px;font-weight:500;margin-bottom:30px}
.service-list{display:flex;gap:70px}
.service{width:180px}
.service .icon{width:46px;height:38px;margin-bottom:10px;background:var(--purple-light);border-radius:6px;opacity:.85}
.service h3{font-size:15px;font-weight:600;color:var(--ink)}
.service p{font-size:12px;color:var(--muted);line-height:1.5}

/* about */
.about{height:580px;position:relative;background:var(--soft)}
.about-art{position:absolute;left:70px;top:60px;width:520px;height:460px;border-radius:50% 50% 46% 54%/56% 50% 50% 44%;background:radial-gradient(circle at 55% 55%,#7cc24a 0%,#9bcb3c 35%,#e9f2dd 70%,var(--soft) 100%)}
.about-text{position:absolute;left:640px;top:110px;width:480px}
.about-text h2{font-family:"Bitter",Georgia,serif;color:var(--green);font-size:26px;font-weight:500;margin-bottom:14px}
.about-text p{font-size:13px;color:var(--muted);margin-bottom:24px}

/* treatments */
.treatments{height:420px;position:relative;background:linear-gradient(90deg,#3c4a2a 0%,#6a7a3f 40%,#8a7550 70%,#4b5a30 100%)}
.treatments .panel{position:absolute;left:220px;top:70px;width:760px;height:270px;background:rgba(30,30,30,.62);padding:30px 50px;color:#fff;text-align:center}
.treatments h2{font-family:"Bitter",Georgia,serif;font-weight:500;font-size:30px;margin-bottom:14px}
.treatments p{font-size:13px;margin-bottom:22px;text-align:left}

/* columns */
.columns{height:460px;position:relative}
.col{position:absolute;top:70px;width:460px}
.col.left{left:110px}
.col.right{left:640px;width:330px}
.col h2{font-family:"Bitter",Georgia,serif;color:var(--green);font-size:26px;font-weight:500;line-height:1.3;margin-bottom:16px}
.col p{font-size:13px;color:var(--muted);margin-bottom:10px}
.col .note{color:var(--green);font-weight:600}
.col ul{list-style:none;font-size:13px;color:var(--muted);margin:4px 0 22px}
.col li{display:flex;align-items:center;gap:8px}
.col .btn{margin-top:14px}
.flower-art{position:absolute;left:985px;top:140px;width:180px;height:260px;border-radius:40%;background:radial-gradient(circle at 50% 45%,#d9a6d4 0%,#ecd3ea 45%,#fff 75%)}

/* partners */
.partners{height:150px;border-top:1px solid #ececec;display:flex;align-items:center;justify-content:center;gap:70px}
.badge{width:110px;height:80px;border-radius:8px;background:#e3e7df}
.badge.round{width:80px;border-radius:50%}

/* footer */
.footer{height:204px;background:var(--footer);color:#ddd;position:relative;font-size:12px}
.footer h4{color:#fff;font-size:15px;font-weight:700;margin-bottom:8px}
.f-links{position:absolute;left:40px;top:18px;display:grid;grid-template-columns:130px 130px;column-gap:20px;line-height:1.75}
.f-links h4{grid-column:1/3}
.f-contact{position:absolute;left:400px;top:18px;width:560px}
.f-contact .row{display:flex;gap:40px;line-height:1.75}
.f-contact .item{display:flex;gap:8px;align-items:flex-start}
.f-contact .item svg{margin-top:4px;flex:none}
.copy{position:absolute;left:0;right:0;bottom:0;height:26px;background:var(--footer-deep);color:#aaa;font-size:11px;padding:5px 40px}
</style>
</head>
<body>

<div class="topbar">
  <span><svg width="12" height="12" viewBox="0 0 24 24"><rect x="2" y="5" width="20" height="14" rx="2" fill="none" stroke="#fff" stroke-width="2"/><path d="M2 6l10 7 10-7" fill="none" stroke="#fff" stroke-width="2"/></svg>info@brackettgrounds.co.uk</span>
  <div class="call">01632 960 418</div>
</div>

<header class="header">
  <div class="tagline">Expert Garden Maintenance Services for Yorkshire</div>
  <div class="brand"><i></i><b>Brackett<br>Grounds</b></div>
  <nav class="nav">
    <a class="active">Home</a><a>About Us</a><a>Residential Services</a><a>Commercial</a><a>Ground Maintenance</a><a>Garden Advice</a><a>Gallery</a><a>Testimonials</a>
  </nav>
</header>

<section class="hero" role="img" aria-label="Photo of a garden bed with spring flowers, terracotta pots and a trowel">
  <div class="hero-text">
    <h1>Always Reliable, Knowledgeable, Friendly &amp; Professional.</h1>
    <p>Providing outstanding garden maintenance to homes and businesses across Yorkshire for over twenty years.</p>
    <a class="btn btn-green">Testimonials</a>
  </div>
</section>

<section class="services">
  <div class="eyebrow">HOW WE HELP</div>
  <h2>Good solutions for your gardens!</h2>
  <div class="service-list">
    <div class="service"><div class="icon" role="img" aria-label="Lawn mower icon"></div><h3>Lawn Mowing</h3><p>Neat, healthy lawns cut on a regular schedule.</p></div>
    <div class="service"><div class="icon" role="img" aria-label="Pruning shears icon"></div><h3>Pruning</h3><p>Shrubs and hedges shaped for strong new growth.</p></div>
    <div class="service"><div class="icon" role="img" aria-label="Weeding tool icon"></div><h3>Weeding</h3><p>Beds kept clear so your plants can thrive.</p></div>
    <div class="service"><div class="icon" role="img" aria-label="Planting and design icon"></div><h3>Planting &amp; design</h3><p>Fresh borders planned and planted to suit you.</p></div>
  </div>
</section>

<section class="about">
  <div class="about-art" role="img" aria-label="Illustration of a gardener tending a young tree among leafy plants"></div>
  <div class="about-text">
    <h2>About Brackett Grounds Services Ltd</h2>
    <p>Brackett Grounds Services Ltd is based in Yorkshire and is a family owned and run business. Our gardening team is committed to providing exceptional service and maintaining high standards. We look after lawns, borders, hedges and patios for homeowners and businesses, and we take pride in leaving every garden tidier than we found it.</p>
    <a class="btn btn-purple">Read More</a>
  </div>
</section>

<section class="treatments" role="img" aria-label="Photo of a sunlit lawn with a garden hat and watering can">
  <div class="panel">
    <h2>Expert Treatment Services</h2>
    <p>Our lawn specialists offer a full range of treatments to keep your grass green and healthy all year. From feeding and weed control to aeration and scarification, we tailor every visit to your lawn and report back after each one.</p>
    <a class="btn btn-green">View Packages</a>
  </div>
</section>

<section class="columns">
  <div class="col left">
    <h2>Regular Garden Maintenance -<br>Fully Booked!</h2>
    <p>We are afraid our regular garden maintenance rounds are fully booked for this season. Please get in touch to join our waiting list and we will contact you as soon as space becomes available.</p>
    <p class="note">Apologies for any disappointment.</p>
    <a class="btn btn-purple">Expert Lawn Care</a>
  </div>
  <div class="col right">
    <h2>Gardening jobs throughout<br>the seasons...</h2>
    <p>What we're doing this month:</p>
    <ul>
      <li><svg width="10" height="10" viewBox="0 0 10 10"><path d="M1 5l3 3 5-6" fill="none" stroke="#3f9a3a" stroke-width="2"/></svg>Spring lawn feeds</li>
      <li><svg width="10" height="10" viewBox="0 0 10 10"><path d="M1 5l3 3 5-6" fill="none" stroke="#3f9a3a" stroke-width="2"/></svg>Hedge and shrub pruning</li>
      <li><svg width="10" height="10" viewBox="0 0 10 10"><path d="M1 5l3 3 5-6" fill="none" stroke="#3f9a3a" stroke-width="2"/></svg>Border weeding</li>
      <li><svg width="10" height="10" viewBox="0 0 10 10"><path d="M1 5l3 3 5-6" fill="none" stroke="#3f9a3a" stroke-width="2"/></svg>Patio cleaning</li>
    </ul>
    <a class="btn btn-purple">Garden Advice</a>
  </div>
  <div class="flower-art" role="img" aria-label="Watercolour illustration of pink flowering branches"></div>
</section>

<section class="partners" aria-label="Accreditations">
  <div class="badge round"></div>
  <div class="badge"></div>
  <div class="badge round"></div>
  <div class="badge"></div>
  <div class="badge"></div>
  <div class="badge"></div>
</section>

<footer class="footer">
  <div class="f-links">
    <h4>Important Links</h4>
    <span>Home</span><span>Garden Advice</span>
    <span>About</span><span>Gallery</span>
    <span>Residential Services</span><span>Testimonials</span>
    <span>Commercial Services</span><span>Contact Us</span>
    <span>Lawn Care</span><span>Privacy Policy</span>
  </div>
  <div class="f-contact">
    <h4>Contact Us</h4>
    <div class="row">
      <div class="item"><svg width="12" height="14" viewBox="0 0 24 28"><path d="M12 1C6 1 2 5.5 2 11c0 7 10 16 10 16s10-9 10-16C22 5.5 18 1 12 1z" fill="#9bcb3c"/><circle cx="12" cy="11" r="4" fill="#2b2b2b"/></svg><span>Brackett Grounds Services Ltd<br>Unit 4, Moorside Farm<br>Fenby Lane, Yorkshire<br>YO99 4QT</span></div>
      <div>
        <div class="item"><svg width="12" height="12" viewBox="0 0 24 24"><rect x="2" y="5" width="20" height="14" rx="2" fill="none" stroke="#9bcb3c" stroke-width="2"/><path d="M2 6l10 7 10-7" fill="none" stroke="#9bcb3c" stroke-width="2"/></svg>info@brackettgrounds.co.uk</div>
        <div class="item"><svg width="12" height="12" viewBox="0 0 24 24"><path d="M6 2l4 4-3 3c1.5 3 4 5.5 7 7l3-3 4 4-3 4C10 21 3 14 2 5z" fill="#9bcb3c"/></svg>01632 960 418</div>
        <div>Company Reg: 09184552</div>
        <div>VAT Registration No: GB 418 2267 90</div>
      </div>
    </div>
  </div>
  <div class="copy">© Copyright Brackett Grounds Services Ltd</div>
</footer>

</body>
</html>
```